8.5"x11" Flatsheets Layout Design for Brookline Herd Inc.

We need a layout for three complimentary 8.5"x11" portrait size flatsheet designs. The flatsheets will be used for our customer testimonials, company profile and product sheet. Therefore we require either an .ai or .eps file so that we can drop in new customer photos, text, pull quotes or other information as required.

Company Profile Layout
- two photos (one of a dairy drinking water in a barn, and one of our system (see satisfied customer.jpg attached).
- area for copy - four equal groups to explain each of our four segments of business (source, science, system, and success). Each segments will have a square icon as the graphical reference (currently being designed on PixelGuild). Each segment will require between 50 to 75 words per section.

Customer Testimonial Layout
- one photo of our system with/without (see attached file satisfied customer) the farmer and one short but wide photo of the barn (see attached KLM dairies).
- Brookline Herd Logo
- 20-40 word pull quote
- 75 word introduction paragraph
- 75 word system benefits paragraph
- Table with 2 columns and 5 rows (first column will have text, second numbers)
(we have attached sample photos and text for three dairies)

Product Layout
- a photo of a cow with a big bulging udder drinking water (see cow udder .jpg - something like this butter better resolution).
-a photo of our system in portrait or landscape (see attached product shot 1 and product shot 2).
- Brookline Herd logo
- 20-40 word pull quote with a 50 word informational parpagraph x 3
- Table with 5 Rows and 3 Columns to contain model number, flow rate, and price. This needs to be in close proximity and related to our product shot.

Common to all Flatsheets

We want a "for more information contact" piece
Brookline Herd Inc.
3158 - 27th Ave NW
Edmonton, Alberta, Canada
T6K 2R8
(780) 214-8907
info@brooklineherd.example
www.brooklineherd.example

We want a lot of white space with some nice blue compliments (same or complimentary colors to our logo).

We want four icons lined up in a row, column or square (icons currently being designed on this site). We want the system icon highlighted in the product flat sheet, and we want to success icon highlighted in the customer testimonial flat sheet, we want either all or none of the icons highlighted on our company profile sheet.
Updates

we have uploaded one set of icons we will be using in our materials to help you with your designs.

We are still looking for new submissions.

Thanks,
Brookline Herd

Reason: We are not currently satisfied with the designs submitted and are seeking additional submissions.

Target Market(s)

The target market for this information is the western Canadian dairy farmer.

For more understanding of this project see Brookline Herd - Icon Design Project.

Industry/Entity Type

Landscape

Requirements
Must have
• We use Calibri as our standard font in all our corporate literature, however we are open to suggestions.
Nice to have
• Most of this information will be distributed electronically via email or website download so please format the sheets to be easily printed considering printer margin issues.

Should not have
• We will be printing these sheets on demand at our shop so please do not include a full bleed but account for a white margin.

```html
<!DOCTYPE html>
<html lang="en">
<head>
<meta charset="utf-8">
<title>Brookline Herd Inc. – Flatsheets</title>
<link rel="stylesheet" href="https://fonts.googleapis.com/css2?family=Carlito:ital,wght@0,400;0,700;1,400&display=swap">
<style>
  :root{
    --page:#f2f4f6;
    --sky:#3aa0e6;
    --blue:#1f7bcd;
    --blue-deep:#1d5fa8;
    --navy:#2d4f86;
    --navy-deep:#243d6e;
    --ink:#1d2f55;
    --orange:#f7941d;
    --orange-light:#ffb347;
    --orange-text:#f59a1b;
    --white:#ffffff;
    --line:#d6dde5;
  }
  *{box-sizing:border-box;margin:0;padding:0}
  html,body{width:1200px;height:900px;overflow:hidden}
  body{background:var(--page);font-family:"Carlito",Calibri,Arial,sans-serif;color:var(--ink);position:relative}

  .sheet{position:absolute;top:202px;width:384px;height:496px;
    background:linear-gradient(180deg,var(--sky) 0%,var(--blue) 60%,var(--blue-deep) 100%);
    border:1px solid var(--line);overflow:hidden}
  .sheet--profile{left:12px}
  .sheet--product{left:408px}
  .sheet--testimonial{left:804px}

  .sheet__title{position:absolute;top:6px;left:0;right:0;text-align:center;
    font-size:19px;font-weight:700;color:var(--orange-text);
    text-shadow:0 1px 0 #8a4a00,0 0 2px rgba(0,0,0,.35)}
  .sheet__dot{position:absolute;top:9px;right:96px;width:14px;height:14px;border-radius:50%;background:var(--white)}

  .sheet__card{position:absolute;top:34px;left:10px;right:10px;height:404px;background:var(--white);border-radius:12px;overflow:hidden}

  .photo{position:absolute;border:2px solid var(--blue);border-radius:8px}
  .photo--barn-room{background:linear-gradient(135deg,#c9d0d6,#8d9aa5 60%,#5f6b74)}
  .photo--system-room{background:linear-gradient(135deg,#6d7580,#b9c4cc 50%,#2c3f66)}
  .photo--herd{background:linear-gradient(160deg,#9aa3ab,#4b4f55 45%,#1e1f22 70%,#c9c3b8)}
  .photo--unit{background:linear-gradient(180deg,#2c3f7a,#3b5fa8 50%,#b7bec6);border-color:transparent;border-radius:4px}
  .photo--farm{background:linear-gradient(180deg,#cfe1f2 0%,#dbe7f1 45%,#6d7f4a 55%,#b58d4e 100%)}
  .photo--farmer{background:linear-gradient(135deg,#8d9aa5,#3d5a3a 45%,#7fb6d9)}

  .seg-icon{position:absolute;width:30px;height:24px;border-radius:6px;
    background:linear-gradient(180deg,var(--orange-light),var(--orange));box-shadow:0 1px 2px rgba(0,0,0,.3)}

  .band{position:absolute;left:0;right:0;color:var(--white);font-size:7px;line-height:1.3;
    background:linear-gradient(90deg,var(--blue),var(--blue-deep));display:flex;gap:10px;padding:6px 10px}
  .band--deep{background:linear-gradient(90deg,var(--blue-deep),var(--navy-deep))}
  .band p{flex:1}
  .band--center{text-align:center;display:block;font-size:7.5px}

  .copy{position:absolute;font-size:7.5px;line-height:1.3;color:var(--ink)}
  .copy--justify{text-align:justify}
  .cols{position:absolute;display:flex;gap:10px;font-size:6.8px;line-height:1.3;color:var(--blue-deep)}
  .cols p{flex:1}
  .quotes{position:absolute;display:flex;gap:10px;font-size:6.8px;line-height:1.3;font-style:italic;color:var(--ink)}
  .quotes figure{flex:1}
  .quotes figcaption{text-align:right;font-size:6.5px}

  .spec{position:absolute;border:5px solid var(--orange);border-left-width:2px;border-bottom-width:2px;border-radius:14px 14px 0 0;background:var(--white);padding:4px}
  .spec table{width:100%;height:100%;border-collapse:collapse;font-size:8px;font-weight:700;color:var(--ink)}
  .spec td{border:1px solid var(--orange);text-align:center;padding:0 3px}
  .spec--two td:first-child{font-size:7px;line-height:1.1;width:55%}
  .spec--two td:last-child{font-size:10px}

  .caption-box{position:absolute;border:2px solid var(--blue);border-radius:8px;overflow:hidden;background:var(--blue)}
  .caption-box .photo{position:static;display:block;border:none;border-radius:0;height:84px}
  .caption-box p{color:var(--white);font-size:6.5px;font-style:italic;padding:4px 6px;line-height:1.25}
  .caption-box cite{display:block;text-align:right;font-size:6px}

  .brand{position:absolute;width:116px;height:34px;border:1px solid var(--blue);border-radius:6px;background:var(--white);
    display:flex;align-items:center;gap:5px;padding:0 8px;font-size:13px;font-weight:700;color:var(--navy);white-space:nowrap}
  .brand__mark{width:10px;height:10px;background:var(--blue)}

  .footer{position:absolute;left:0;right:0;bottom:0;height:58px;background:linear-gradient(180deg,var(--navy),var(--navy-deep));color:var(--white)}
  .footer__web{position:absolute;left:10px;top:20px;font-size:9px;font-weight:700;white-space:nowrap}
  .footer__mid{position:absolute;left:140px;width:104px;top:4px;text-align:center;white-space:nowrap}
  .footer__name{font-size:8.5px;font-weight:700;color:var(--orange-text)}
  .footer__phone{font-size:12px;font-weight:700;line-height:1.15}
  .footer__city{font-size:6.5px;font-weight:700;color:var(--orange-text)}
  .footer__mail{position:absolute;right:10px;top:20px;font-size:8px;font-weight:700;white-space:nowrap}
  .footer__street{position:absolute;left:10px;bottom:4px;font-size:6.5px;font-weight:700;color:var(--orange-text)}
  .footer__post{position:absolute;right:10px;bottom:4px;font-size:6.5px;font-weight:700;color:var(--orange-text)}
</style>
</head>
<body>

<!-- Company Profile -->
<section class="sheet sheet--profile">
  <h1 class="sheet__title">Company Profile</h1><span class="sheet__dot"></span>
  <div class="sheet__card">
    <div class="photo photo--barn-room" role="img" aria-label="Photo of a water treatment room with tanks and controls" style="left:8px;top:14px;width:166px;height:110px"></div>
    <div class="photo photo--system-room" role="img" aria-label="Photo of a farmer standing beside the water system" style="left:184px;top:14px;width:172px;height:110px"></div>
    <span class="seg-icon" style="left:66px;top:148px"></span>
    <span class="seg-icon" style="left:258px;top:148px"></span>
    <div class="band" style="top:176px;height:56px">
      <p>one two three four five six seven eight nine ten, one two three four five six seven eight nine ten, one two three four five six seven eight nine ten, one two three four five six seven eight nine ten</p>
      <p>one two three four five six seven eight nine ten, one two three four five six seven eight nine ten, one two three four five six seven eight nine ten, one two three four five six seven eight nine ten</p>
    </div>
    <span class="seg-icon" style="left:66px;top:246px"></span>
    <span class="seg-icon" style="left:258px;top:246px"></span>
    <div class="band band--deep" style="top:274px;height:56px">
      <p>one two three four five six seven eight nine ten, one two three four five six seven eight nine ten, one two three four five six seven eight nine ten, one two three four five six seven eight nine ten</p>
      <p>one two three four five six seven eight nine ten, one two three four five six seven eight nine ten, one two three four five six seven eight nine ten, one two three four five six seven eight nine ten</p>
    </div>
    <div class="brand" style="left:240px;top:356px"><span class="brand__mark"></span>Brookline Herd</div>
  </div>
  <footer class="footer">
    <span class="footer__web">www.brooklineherd.example</span>
    <div class="footer__mid"><div class="footer__name">Brookline Herd Inc.</div><div class="footer__phone">(780) 214-8907</div><div class="footer__city">Edmonton, Alberta, Canada</div></div>
    <span class="footer__mail">info@brooklineherd.example</span>
    <span class="footer__street">3158 - 27th Ave NW</span><span class="footer__post">T6K 2R8</span>
  </footer>
</section>

<!-- Product -->
<section class="sheet sheet--product">
  <h1 class="sheet__title">Product</h1><span class="sheet__dot" style="right:130px"></span>
  <div class="sheet__card">
    <span class="seg-icon" style="left:80px;top:12px"></span>
    <p class="copy copy--justify" style="left:8px;top:44px;width:174px">one two three four five six seven eight nine ten, one two three four five six seven eight nine ten, one two three four five six seven eight nine ten, one two three four five six seven eight nine ten, one two three four five six seven eight nine ten, one two three four five six seven eight nine ten</p>
    <div class="photo photo--herd" role="img" aria-label="Photo of dairy cows resting in a free-stall barn" style="left:190px;top:8px;width:166px;height:110px"></div>
    <div class="photo photo--unit" role="img" aria-label="Product photo of the water treatment unit" style="left:12px;top:132px;width:72px;height:122px"></div>
    <div class="spec" style="left:98px;top:124px;width:258px;height:136px">
      <table>
        <tr><td>Model 1</td><td>15 GPM</td><td>$ 9,950</td></tr>
        <tr><td>Model 2</td><td>15 GPM</td><td>$ 12,990</td></tr>
        <tr><td>Model 3</td><td>30 GPM</td><td>$ 15, 490</td></tr>
        <tr><td>Model 4</td><td>60 GPM</td><td>$ 19,990</td></tr>
        <tr><td>Model 5</td><td>60 GPM</td><td>$ 24,590</td></tr>
      </table>
    </div>
    <div class="cols" style="left:8px;right:8px;top:266px">
      <p>one two three four five six seven eight nine ten, one two three four five six seven eight nine ten, one two three four five six seven eight nine ten</p>
      <p>one two three four five six seven eight nine ten, one two three four five six seven eight nine ten, one two three four five six seven eight nine ten</p>
      <p>one two three four five six seven eight nine ten, one two three four five six seven eight nine ten, one two three four five six seven eight nine ten</p>
    </div>
    <div class="quotes" style="left:8px;right:8px;top:318px">
      <figure><blockquote>“one two three four five six seven eight nine ten, one two three four five six.”</blockquote><figcaption>~ Ned Farrow</figcaption></figure>
      <figure><blockquote>“one two three four five six seven eight nine ten, one two three four.”</blockquote><figcaption>~ Hollis Grange</figcaption></figure>
      <figure><blockquote>“one two three four five six seven eight, one two three.”</blockquote><figcaption>~ Cal Rennick</figcaption></figure>
    </div>
    <div class="brand" style="left:240px;top:362px"><span class="brand__mark"></span>Brookline Herd</div>
  </div>
  <footer class="footer">
    <span class="footer__web">www.brooklineherd.example</span>
    <div class="footer__mid"><div class="footer__name">Brookline Herd Inc.</div><div class="footer__phone">(780) 214-8907</div><div class="footer__city">Edmonton, Alberta, Canada</div></div>
    <span class="footer__mail">info@brooklineherd.example</span>
    <span class="footer__street">3158 - 27th Ave NW</span><span class="footer__post">T6K 2R8</span>
  </footer>
</section>

<!-- Testimonial -->
<section class="sheet sheet--testimonial">
  <h1 class="sheet__title">Testimonial</h1><span class="sheet__dot" style="right:108px"></span>
  <div class="sheet__card">
    <div class="photo photo--farm" role="img" aria-label="Wide photo of a dairy farm and field under a pale sky" style="left:8px;top:10px;width:348px;height:94px"></div>
    <span class="seg-icon" style="left:8px;top:114px"></span>
    <p class="copy" style="left:44px;top:112px;width:314px;text-align:center">one two three four five six seven eight nine ten, one two three four five six seven eight nine ten, one two three four five six seven eight nine ten, one two three four five six seven eight nine ten, one two three four five six seven eight nine ten, one two three four five six seven eight nine ten, one two three four five</p>
    <div class="band band--center" style="top:166px;height:46px">one two three four five six seven eight nine ten, one two three four five six seven eight nine ten, one two three four five six seven eight nine ten, one two three four five six seven eight nine ten, one two three four five six seven eight nine ten, one two three four five six seven eight nine ten</div>
    <div class="caption-box" style="left:8px;top:222px;width:128px;height:132px">
      <div class="photo photo--farmer" role="img" aria-label="Photo of a dairy farmer beside his water system"></div>
      <p>Our system resulted in high quality water and required less chlorine, acid and cleaner.<cite>~ Dirk Vanterpool, Marsh Creek Dairy</cite></p>
    </div>
    <div class="spec spec--two" style="left:146px;top:222px;width:210px;height:126px">
      <table>
        <tr><td>Text, text and more text in this box.</td><td>15 GPM</td></tr>
        <tr><td>Text, text and more text in this box.</td><td>15 GPM</td></tr>
        <tr><td>Text, text and more text in this box.</td><td>60 GPM</td></tr>
        <tr><td>Text, text and more text in this box.</td><td>60 GPM</td></tr>
        <tr><td>Text, text and more text in this box.</td><td>60 GPM</td></tr>
      </table>
    </div>
    <div class="brand" style="left:240px;top:362px"><span class="brand__mark"></span>Brookline Herd</div>
  </div>
  <footer class="footer">
    <span class="footer__web">www.brooklineherd.example</span>
    <div class="footer__mid"><div class="footer__name">Brookline Herd Inc.</div><div class="footer__phone">(780) 214-8907</div><div class="footer__city">Edmonton, Alberta, Canada</div></div>
    <span class="footer__mail">info@brooklineherd.example</span>
    <span class="footer__street">3158 - 27th Ave NW</span><span class="footer__post">T6K 2R8</span>
  </footer>
</section>

</body>
</html>
```